web site for Biblical Oils, Candles and Perfumes

To make a web design with "magento".
To show image of the company/products and to be a shop.
see sample:
www.morvatlu.ws
it is important that we will have pages of description of the products category
then puctures with item description and option to select how many to add to the cart.
Special reduction on product or full category.
Managing clients with possibility to give special reduction to specific client.
each product can be see in bigger image.
can write more information about the product.

Target Market(s)

christian, evangelist, bible lover, belivers

Industry/Entity Type

It Company

Number of Pages Required

5+ page

Requirements
Must have
• my possibility to maintains the web-site by myself (wordpree workers)
Nice to have
• to have statitics

```html
<!DOCTYPE html>
<html lang="en">
<head>
<meta charset="utf-8">
<title>Morvani Oils – Oils, Candles and Perfumes</title>
<link rel="stylesheet" href="https://fonts.googleapis.com/css2?family=Open+Sans:wght@400;600;700&family=Raleway:wght@400;600;800&display=swap">
<style>
:root{
  --brand:#e8515b;
  --ink:#333333;
  --muted:#8a8a8a;
  --line:#e4e4e4;
  --paper:#ffffff;
  --band:#f1f1f1;
  --footer:#1f1f1f;
  --footer-deep:#161616;
  --footer-text:#a8a8a8;
  --hero-a:#f4ebe1;
  --hero-b:#e9dccd;
}
*{margin:0;padding:0;box-sizing:border-box}
html,body{width:692px;height:1200px;overflow:hidden}
body{font-family:"Open Sans",Arial,sans-serif;color:var(--ink);background:var(--paper);font-size:9px}
.top-bar{height:36px;background:var(--brand);color:#fff;display:flex;align-items:center;justify-content:space-between;padding:0 22px;font-size:8px}
.top-bar .left{display:flex;gap:14px}
.top-bar .right{display:flex;gap:12px}
.site-header{height:46px;display:flex;align-items:center;justify-content:space-between;padding:0 22px;border-bottom:1px solid var(--line)}
.logo{font-family:"Raleway",Arial,sans-serif;font-size:19px;font-weight:600;color:var(--ink);letter-spacing:.2px}
.header-right{display:flex;align-items:center;gap:10px}
.main-nav{display:flex;gap:4px}
.main-nav a{font-size:8px;color:var(--ink);text-decoration:none;padding:6px 10px}
.main-nav a.active{background:var(--brand);color:#fff}
.icon-btn{width:22px;height:22px;display:flex;align-items:center;justify-content:center;border:1px solid var(--line)}
.icon-btn.cart{background:var(--brand);border-color:var(--brand);border-radius:50%}
.hero{position:relative;height:288px;background:linear-gradient(90deg,var(--hero-a) 0%,#f7f0e8 45%,var(--hero-b) 100%);overflow:hidden}
.hero-photo{position:absolute;right:0;top:0;width:62%;height:100%;background:radial-gradient(ellipse at 55% 45%,#f2d9c7 0%,#ecd7c6 35%,#e6dbd0 70%,rgba(244,235,225,0) 100%)}
.hero-copy{position:absolute;left:34px;top:110px}
.hero-kicker{font-size:12px;color:#6b6460;margin-bottom:6px}
.hero-title{font-family:"Raleway",Arial,sans-serif;font-weight:800;font-size:33px;color:#e46a3c;letter-spacing:1px;margin-bottom:18px}
.hero-btn{display:inline-block;background:#fff;color:var(--ink);font-size:8px;font-weight:600;padding:8px 12px}
.featured{padding:18px 46px 0}
.section-head{display:flex;justify-content:space-between;align-items:flex-end;border-bottom:1px solid var(--line);margin-bottom:14px}
.section-title{font-family:"Raleway",Arial,sans-serif;font-size:15px;font-weight:600;color:var(--brand);padding-bottom:6px;border-bottom:2px solid var(--brand);margin-bottom:-1px}
.section-arrows{color:#bbb;font-size:10px;padding-bottom:6px;letter-spacing:4px}
.product-grid{display:grid;grid-template-columns:repeat(4,1fr);gap:18px 14px}
.product-card{border:1px solid var(--line);height:198px;display:flex;flex-direction:column}
.product-image{height:128px;margin:8px 8px 6px;display:flex;align-items:center;justify-content:center}
.product-image span{display:block;width:70px;height:80px;border-radius:4px}
.product-name{font-size:8px;font-weight:600;padding:4px 8px 8px}
.product-foot{margin-top:auto;display:flex;border-top:1px solid var(--line);height:28px;align-items:center;font-size:8px}
.price{font-weight:700;padding:0 8px;border-right:1px solid var(--line);height:100%;display:flex;align-items:center}
.add-cart{padding-left:8px;color:var(--muted)}
.testimonials{margin-top:20px;background:var(--band);height:124px;padding:12px 46px 0;position:relative}
.testimonials h3{font-size:8px;font-weight:700;margin-bottom:14px}
.quotes{display:flex;gap:30px}
.quote{display:flex;gap:14px;flex:1}
.avatar{width:42px;height:42px;border-radius:50%;background:linear-gradient(135deg,#c9b8a8,#8d7b6c);flex:none}
.quote p{font-size:7px;line-height:1.5;color:var(--muted)}
.quote .who{color:var(--brand);font-size:7px;margin-top:4px}
.dots{position:absolute;bottom:10px;left:0;right:0;display:flex;justify-content:center;gap:6px}
.dots i{width:5px;height:5px;border-radius:50%;background:#ccc}
.dots i.on{background:var(--brand)}
.site-footer{background:var(--footer);height:124px;padding:20px 46px 0;display:grid;grid-template-columns:1.3fr 1fr 1fr 1.2fr;gap:18px;color:var(--footer-text);font-size:7px}
.site-footer .logo{font-size:15px;color:#d9d9d9;font-weight:400;margin-bottom:8px}
.site-footer h4{color:#fff;font-size:8px;font-weight:700;margin-bottom:8px}
.site-footer li{list-style:none;line-height:1.75}
.site-footer p{line-height:1.6}
.footer-bottom{background:var(--footer-deep);height:70px;display:flex;flex-direction:column;align-items:center;justify-content:center;gap:8px;color:var(--footer-text);font-size:7px}
.footer-links{display:flex;gap:8px}
.social{display:flex;gap:6px}
.social i{width:14px;height:14px;border-radius:50%;background:#444}
</style>
</head>
<body>
<div class="top-bar">
  <div class="left"><span>Default welcome msg!</span><span>sales@morvanioils.ws</span></div>
  <div class="right"><span>USD ▾</span><span>English ▾</span><span>Login</span></div>
</div>
<header class="site-header">
  <div class="logo">Morvani Oils</div>
  <div class="header-right">
    <nav class="main-nav">
      <a class="active" href="#">Home</a><a href="#">About Us</a><a href="#">Help</a><a href="#">Contact Us</a>
    </nav>
    <div class="icon-btn"><svg width="10" height="10" viewBox="0 0 10 10"><circle cx="4" cy="4" r="3" fill="none" stroke="#333" stroke-width="1.2"/><line x1="6.2" y1="6.2" x2="9" y2="9" stroke="#333" stroke-width="1.2"/></svg></div>
    <div class="icon-btn cart"><svg width="10" height="10" viewBox="0 0 10 10"><path d="M1 2h1.5l1 5h4.5l1-3.5H3" fill="none" stroke="#fff" stroke-width="1"/><circle cx="4" cy="8.6" r=".8" fill="#fff"/><circle cx="7.5" cy="8.6" r=".8" fill="#fff"/></svg></div>
  </div>
</header>
<section class="hero">
  <div class="hero-photo" role="img" aria-label="Portrait photo of a woman holding a white lily against a soft neutral background"></div>
  <div class="hero-copy">
    <div class="hero-kicker">Lookbook Collection 15/16</div>
    <div class="hero-title">NATURAL BEAUTY</div>
    <span class="hero-btn">PURCHASE NOW</span>
  </div>
</section>
<section class="featured">
  <div class="section-head"><h2 class="section-title">Featured Products</h2><span class="section-arrows">‹ ›</span></div>
  <div class="product-grid">
    <div class="product-card"><div class="product-image" role="img" aria-label="Product photo of a gold cosmetic jar"><span style="background:linear-gradient(#e6c97a,#b8923e);border-radius:50%;width:80px;height:60px"></span></div><div class="product-name">Abidos Multivitamin...</div><div class="product-foot"><span class="price">$200.00</span><span class="add-cart">+ Add to Cart</span></div></div>
    <div class="product-card"><div class="product-image" role="img" aria-label="Product photo of a boxed oil bottle"><span style="background:linear-gradient(#6a8fc7,#2f4f8c)"></span></div><div class="product-name">Acelo Sera Tab</div><div class="product-foot"><span class="price">$200.00</span><span class="add-cart">+ Add to Cart</span></div></div>
    <div class="product-card"><div class="product-image" role="img" aria-label="Product photo of a perfume bottle with a gift box"><span style="background:linear-gradient(#f1e7b8,#c9b36a)"></span></div><div class="product-name">Skin Care Lip Care</div><div class="product-foot"><span class="price">$200.00</span><span class="add-cart">+ Add to Cart</span></div></div>
    <div class="product-card"><div class="product-image" role="img" aria-label="Product photo of a bar of soap"><span style="background:linear-gradient(#d9a7a0,#a8766e);height:50px;width:80px"></span></div><div class="product-name">Cocoflofo Pillibottle...</div><div class="product-foot"><span class="price">$200.00</span><span class="add-cart">+ Add to Cart</span></div></div>
    <div class="product-card"><div class="product-image" role="img" aria-label="Product photo of a set of oil vials"><span style="background:linear-gradient(#e7b27a,#b9773f);height:50px;width:90px"></span></div><div class="product-name">Abidos Multivitamin...</div><div class="product-foot"><span class="price">$200.00</span><span class="add-cart">+ Add to Cart</span></div></div>
    <div class="product-card"><div class="product-image" role="img" aria-label="Product photo of an anointing oil bottle and box"><span style="background:linear-gradient(#f0c24c,#b27e1c)"></span></div><div class="product-name">Acelo Sera Tab</div><div class="product-foot"><span class="price">$200.00</span><span class="add-cart">+ Add to Cart</span></div></div>
    <div class="product-card"><div class="product-image" role="img" aria-label="Product photo of a gift set of three oils"><span style="background:linear-gradient(#d8d3c6,#8c8576);width:90px;height:60px"></span></div><div class="product-name">Skin Care Lip Care</div><div class="product-foot"><span class="price">$200.00</span><span class="add-cart">+ Add to Cart</span></div></div>
    <div class="product-card"><div class="product-image" role="img" aria-label="Product photo of a gold cosmetic jar"><span style="background:linear-gradient(#e6c97a,#b8923e);border-radius:50%;width:80px;height:60px"></span></div><div class="product-name">Cocoflofo Pillibottle...</div><div class="product-foot"><span class="price">$200.00</span><span class="add-cart">+ Add to Cart</span></div></div>
  </div>
</section>
<section class="testimonials">
  <h3>WHAT PEOPLE SAY</h3>
  <div class="quotes">
    <div class="quote"><div class="avatar" role="img" aria-label="Customer portrait"></div><div><p>The anointing oil arrived quickly and smells wonderful. Lovely packaging, a true blessing for our family and a gift we will order again.</p><div class="who">Sarah Miller<br>Customer</div></div></div>
    <div class="quote"><div class="avatar" role="img" aria-label="Customer portrait"></div><div><p>Beautiful candles and perfumes from the Holy Land. Service was kind and helpful, and every item matched its description perfectly.</p><div class="who">David Cohen<br>Customer</div></div></div>
  </div>
  <div class="dots"><i class="on"></i><i></i><i></i></div>
</section>
<footer>
  <div class="site-footer">
    <div><div class="logo">Morvani Oils</div><p>Oils, candles and perfumes made with care, inspired by the land of the Bible.</p></div>
    <div><h4>CMS BLOCK</h4><ul><li>Customer Assistance</li><li>Customer Guarantee</li><li>Delivery Information</li><li>International Shipping</li></ul></div>
    <div><h4>MY ACCOUNT</h4><ul><li>My Orders</li><li>My Credit Slips</li><li>My Addresses</li><li>My Personal Info</li></ul></div>
    <div><h4>CONTACT US</h4><p>Morvani Oils Ltd, 12 Olive Grove Road, Hill Town 4410<br>Phone: 000-555-0142<br>Fax: 000-555-0143<br>sales@morvanioils.ws</p></div>
  </div>
  <div class="footer-bottom">
    <div class="footer-links"><span>Site Map</span>|<span>Search Terms</span>|<span>Advanced Search</span>|<span>Orders and Returns</span>|<span>Contact Us</span></div>
    <div>© 2015 Morvani Oils Store. All Rights Reserved.</div>
    <div class="social"><i></i><i></i><i></i><i></i><i></i><i></i></div>
  </div>
</footer>
</body>
</html>
```